Need a "Coming Soon" Page

Hi There!

This should be a really simple project - I just need a coming soon page. I've attached my logo and an example of a coming soon page that I think is a good model.

It should appear as follows:

Bluefern Hollow Caregivers
Los Angeles' premier provider of LGBT culturally competent non medical home care for LGBT Seniors and people aging with HIV who need Assistance with Activities of Daily Living and/or companion care services.

Coming in Early 2015

Target Market(s)

Los Angeles based LGBT Seniors (50 years or older) and LA based people aging with HIV.

Industry/Entity Type

Medical

Font styles to use
Serif

Colors
00a98f
34b8a4

Requirements
Must have
• A place to capture the e-mail address of interested persons.

```html
<!DOCTYPE html>
<html lang="en">
<head>
<meta charset="utf-8">
<title>Bluefern Hollow Caregivers — Coming Soon</title>
<link rel="stylesheet" href="https://fonts.googleapis.com/css2?family=Libre+Baskerville:wght@400;700&family=Mulish:wght@400&display=swap">
<style>
  :root {
    --ink-green: #004d40;
    --brand-green: #0b6a45;
    --accent-green: #00a98f;
    --footer-green: #07624f;
    --notify-red: #d9262a;
    --text-dark: #2a2a2a;
    --field-border: #d6d6d6;
    --white: #ffffff;
  }
  * { box-sizing: border-box; margin: 0; padding: 0; }
  html, body { width: 1200px; height: 670px; overflow: hidden; }
  body { position: relative; font-family: "Mulish", sans-serif; background: #cfcac6; }

  .hero-photo {
    position: absolute; left: 0; top: 0; width: 1200px; height: 611px;
    background:
      radial-gradient(ellipse 260px 300px at 520px 150px, #7a4a35 0%, rgba(122,74,53,0) 70%),
      radial-gradient(ellipse 260px 300px at 880px 170px, #e2c8bd 0%, rgba(226,200,189,0) 70%),
      linear-gradient(90deg, #2a2a2a 0%, #3a3533 30%, #8d8783 55%, #9a9a9c 80%, #b7b6b4 100%);
  }

  .signup-panel {
    position: absolute; left: 169px; top: 214px; width: 862px; height: 328px;
    border-radius: 4px;
    background: linear-gradient(180deg, rgba(255,255,255,0.88) 0%, rgba(255,255,255,0.95) 55%, #ffffff 100%);
  }

  .panel-title {
    position: absolute; left: 0; top: 48px; width: 100%;
    text-align: center;
    font-family: "Libre Baskerville", serif; font-weight: 400;
    font-size: 38px; line-height: 1.2; color: var(--ink-green);
  }
  .panel-intro {
    position: absolute; left: 0; top: 103px; width: 100%;
    text-align: center; font-size: 14px; color: var(--text-dark);
  }

  .brand-mark {
    position: absolute; left: 44px; top: 163px; width: 340px; height: 107px;
    display: flex; align-items: center; gap: 14px;
  }
  .brand-mark .brand-dot {
    flex: none; width: 44px; height: 44px; border-radius: 50%;
    background: var(--accent-green);
  }
  .brand-mark .brand-name {
    font-family: "Libre Baskerville", serif; font-weight: 400;
    font-size: 27px; line-height: 1.1; color: var(--brand-green);
  }

  .email-form { position: absolute; left: 464px; top: 171px; width: 349px; }
  .email-field {
    display: flex; align-items: center; gap: 8px;
    height: 50px; padding: 0 14px;
    background: var(--white); border: 1px solid var(--field-border); border-radius: 2px;
  }
  .email-field input {
    border: 0; outline: 0; width: 100%; background: transparent;
    font-family: "Libre Baskerville", serif; font-size: 16px; color: #555;
  }
  .email-field input::placeholder { color: #666; }
  .notify-button {
    display: block; width: 100%; height: 42px; margin-top: 5px;
    border: 0; border-radius: 2px; background: var(--notify-red); color: var(--white);
    font-family: "Libre Baskerville", serif; font-size: 17px; letter-spacing: 0.5px;
  }

  .site-footer {
    position: absolute; left: 0; top: 611px; width: 1200px; height: 59px;
    background: var(--footer-green); color: var(--white);
    display: flex; align-items: center; justify-content: center;
    font-family: "Libre Baskerville", serif; font-size: 12px;
  }
</style>
</head>
<body>
  <div class="hero-photo" role="img" aria-label="Photograph of two smiling senior women sitting close together"></div>

  <section class="signup-panel">
    <h1 class="panel-title">Coming Soon</h1>
    <p class="panel-intro">This is Pictora's version&nbsp; of Lorem Ipsum. Proin gravida nibh vel velit auctor aliquet. Aenean sollicitudin, lorem quis</p>

    <div class="brand-mark">
      <span class="brand-dot"></span>
      <span class="brand-name">Bluefern Hollow Caregivers</span>
    </div>

    <form class="email-form">
      <label class="email-field">
        <svg width="22" height="15" viewBox="0 0 22 15" aria-hidden="true">
          <rect x="0.75" y="0.75" width="20.5" height="13.5" fill="none" stroke="#666" stroke-width="1.2"/>
          <polyline points="1,1 11,9 21,1" fill="none" stroke="#666" stroke-width="1.2"/>
        </svg>
        <input type="email" placeholder="Enter Your Email Address">
      </label>
      <button type="button" class="notify-button">NOTIFY ME</button>
    </form>
  </section>

  <footer class="site-footer">© copyrights 2015 all rights reserved</footer>
</body>
</html>
```